Rolling Nest - Portable Skateboard Display, Organizer, & Stand

Single Webpage for a new company that just launched our first product, the "Rolling Nest Skateboard Stand". This is a consumer product targeted toward parents (especially moms) with kids who have skateboards laying around. Our product is a storage/display/stand that keeps skateboards off of the ground and wheels away from walls. The website design needs to really sell the product as a Portable and Quality product, which can be put anywhere in the home. The website should appeal to adults (Moms especially) and help them quickly understand the versatility, flexibility, high quality, simplicity, and use of the Rolling Nest Skateboard stand. Our website can be viewed at www.rollingnest.example - we'd like to continue to link visitors to our Marketvale product listing for purchases (in the design you submit). Please review the attached creative files and feel free to reach out for additional information.

Target Market(s)

Parents (specifically Moms) with children who own skateboards, interested in keeping a clean and organized home.

Industry/Entity Type

It Company

Number of Pages Required

1 page

Font styles to use
Sans Serif

Requirements
Must have
• Must express the Portability, Quality, and Flexibility of the product. (It can be moved / placed anywhere, does not require mounting or drilling holes)
Nice to have
• Really sell the ease of use and benefit.
Should not have
• Should not be overly complex or cluttered.

```html
<!DOCTYPE html>
<html lang="en">
<head>
<meta charset="utf-8">
<title>Rolling Nest Skateboard Stand</title>
<link href="https://fonts.googleapis.com/css2?family=Open+Sans:wght@400;600;700;800&display=swap" rel="stylesheet">
<style>
:root{
  --navy:#1d3f74;
  --blue:#1a78c8;
  --sky:#29a8e0;
  --cyan:#4cc3ec;
  --red:#e53935;
  --green:#7cc242;
  --page:#eef0f3;
  --ink:#333;
  --muted:#777;
  --line:#d9dde2;
  --foot:#2b2b2b;
  --white:#fff;
}
*{box-sizing:border-box;margin:0;padding:0}
html,body{width:1200px;height:2192px;overflow:hidden}
body{position:relative;font-family:"Open Sans",Arial,sans-serif;color:var(--ink);background:var(--page);font-size:13px}
.abs{position:absolute}
/* header */
.site-header{left:0;top:0;width:1200px;height:136px;background:var(--white)}
.brand{left:152px;top:40px;display:flex;align-items:center;gap:12px}
.brand-mark{width:58px;height:58px;background:var(--blue)}
.brand-name{font-weight:800;font-size:26px;line-height:26px;color:var(--navy)}
.top-links{right:72px;top:10px;display:flex;gap:26px;font-size:12px;color:#555}
.top-links span{display:flex;align-items:center;gap:6px}
.top-links i{width:10px;height:10px;background:var(--navy);border-radius:2px;display:inline-block}
.search{left:592px;top:72px;width:320px;height:28px;display:flex;border:1px solid var(--line)}
.search input{flex:1;border:0;padding:0 10px;font:inherit;font-size:12px;color:#999}
.search button{width:36px;border:0;background:var(--navy)}
.cart{left:1010px;top:60px;width:118px;height:48px;background:var(--sky);display:flex;align-items:center;gap:8px;padding:0 10px;color:var(--white)}
.cart b{color:var(--red);background:var(--white);padding:0 4px;font-size:14px}
.cart small{display:block;font-size:10px}
/* nav */
.main-nav{left:152px;top:136px;width:976px;height:40px;background:var(--navy);display:flex}
.main-nav a{flex:1;text-align:center;line-height:40px;color:var(--white);text-decoration:none;font-size:13px;font-weight:600}
.main-nav a.active{background:var(--sky)}
/* hero */
.hero{left:0;top:176px;width:1200px;height:464px;background:linear-gradient(120deg,#4a3a2e 0%,#7a5a42 45%,#3b4a5a 100%)}
.hero h1{left:152px;top:190px;color:var(--white);font-size:38px;line-height:46px;font-weight:600}
.btn{display:inline-block;background:var(--blue);color:var(--white);font-size:12px;text-align:center}
.hero .btn{left:152px;top:346px;width:180px;height:32px;line-height:32px}
.dots{left:152px;top:432px;display:flex;gap:8px}
.dots i{width:8px;height:8px;border-radius:50%;background:rgba(255,255,255,.5)}
.dots i:first-child{background:var(--white)}
/* welcome */
.sec-title{font-size:16px;color:var(--navy);font-weight:600}
.welcome-title{left:160px;top:694px}
.welcome-box{left:160px;top:724px;width:440px;height:136px;background:var(--white);border:1px solid var(--line);padding:16px 20px}
.welcome-box h3{font-size:12px;font-weight:700;margin-bottom:8px}
.welcome-box p{font-size:11px;line-height:16px;color:var(--muted)}
.welcome-box .more{position:absolute;right:16px;bottom:12px;font-size:11px;color:var(--ink)}
.video-title{left:660px;top:694px;text-decoration:underline}
.video{left:660px;top:722px;width:480px;height:178px;background:linear-gradient(90deg,#5b4a3c,#2e2a28 50%,#6b6660);display:flex;align-items:center;justify-content:center}
/* sidebar promos */
.promo{left:160px;width:192px;color:var(--white);padding:12px;text-align:center}
.promo-clear{top:920px;height:196px;background:linear-gradient(#3d7fc4,#2a5f9a)}
.promo-ship{top:1128px;height:188px;background:var(--navy)}
.promo-dummy{top:1328px;height:212px;background:var(--cyan)}
.promo .label{font-size:11px;font-weight:700;letter-spacing:.5px}
.promo .big{font-size:40px;font-weight:800;line-height:48px}
.promo .ph{height:70px;margin:8px 0;background:linear-gradient(135deg,#dfe7ef,#a9bccd)}
.promo .mini{display:inline-block;background:var(--white);color:var(--navy);font-size:10px;font-weight:700;padding:4px 12px}
/* products */
.popular-bar{left:368px;top:920px;width:772px;height:40px;background:var(--blue);color:var(--white);font-weight:700;font-size:13px;line-height:40px;padding-left:16px}
.grid{left:368px;top:972px;width:772px;display:grid;grid-template-columns:repeat(4,1fr);gap:12px}
.card{position:relative;height:278px;background:var(--white);border:1px solid var(--line);padding:10px}
.card .ph{height:140px;background:var(--tone,linear-gradient(135deg,#f2f4f6,#c9d2da))}
.card .sale{position:absolute;right:10px;top:10px;background:var(--blue);color:var(--white);font-size:9px;font-weight:700;padding:4px 5px}
.card h4{font-size:10px;font-weight:700;margin-top:10px;white-space:nowrap;overflow:hidden;text-overflow:ellipsis}
.card .meta{display:flex;justify-content:space-between;font-size:9px;color:var(--muted);margin-top:4px}
.card .row{display:flex;justify-content:space-between;align-items:center;margin-top:4px}
.card .stars{color:#f0a500;font-size:11px}
.card .price{color:var(--red);font-size:14px;font-weight:700}
.card .actions{position:absolute;left:10px;right:10px;bottom:10px;display:flex;gap:6px}
.card .actions span{flex:1;background:var(--blue);color:var(--white);font-size:10px;text-align:center;line-height:22px}
.card .actions i{width:26px;background:#bbb}
.t-white{--tone:linear-gradient(135deg,#f6f7f9,#cfd9e6 70%,#3a78c0)}
.t-green{--tone:linear-gradient(135deg,#eef6e4,#9fd65a 60%,#6aa83a)}
.t-cream{--tone:linear-gradient(135deg,#f7f4ee,#ddd6c8 70%,#8a8a8a)}
.t-grey{--tone:linear-gradient(135deg,#f1f2f4,#c5cad1 70%,#6f7680)}
.t-red{--tone:linear-gradient(135deg,#fbe9ec,#e2576b 60%,#b52a3c)}
.t-wood{--tone:linear-gradient(135deg,#efe4d4,#b88d5e 60%,#6f5236)}
.t-color{--tone:linear-gradient(135deg,#e9edf2,#6d8fb8 45%,#c46a4a)}
.t-deck{--tone:linear-gradient(135deg,#eceae6,#a49a8c 55%,#4f5560)}
/* newsletter */
.news{left:160px;top:1598px;width:440px}
.news h2{font-size:14px;font-weight:700;color:var(--navy);line-height:22px}
.news h3{font-size:14px;font-weight:700;color:var(--blue);margin-top:10px}
.news p{font-size:11px;line-height:16px;color:var(--muted);margin-top:8px}
.signup{margin-top:18px;background:var(--white);border:1px solid var(--line);padding:12px;display:flex;align-items:center;gap:10px}
.signup .ico{width:40px;height:40px;border-radius:50%;background:var(--navy);flex:none}
.signup .field{flex:1}
.signup .field small{font-size:10px;font-weight:700;display:block;margin-bottom:4px}
.signup .line{display:flex}
.signup .line span{flex:1;border:1px solid var(--line);height:24px}
.signup .line b{background:var(--navy);color:var(--white);font-size:10px;line-height:24px;padding:0 16px}
.news-photo{left:620px;top:1592px;width:520px;height:240px;background:linear-gradient(135deg,#e6d6c0,#8fb3c7 60%,#7a9a4a)}
/* features */
.features{left:160px;top:1862px;width:980px;display:grid;grid-template-columns:repeat(4,1fr);gap:16px}
.feature{height:92px;background:var(--white);border:1px solid var(--line);border-radius:6px;display:flex;align-items:center;gap:14px;padding:0 16px}
.feature .circle{width:52px;height:52px;border-radius:50%;flex:none;display:flex;align-items:center;justify-content:center}
.feature b{display:block;font-size:12px}
.feature small{font-size:10px;color:var(--muted)}
/* footer */
.site-footer{left:0;top:1984px;width:1200px;height:176px;background:var(--foot);color:#ccc}
.foot-col{top:20px;font-size:10px;line-height:16px}
.foot-col h5{color:var(--white);font-size:10px;font-weight:700;margin-bottom:6px}
.map{left:152px;top:20px;width:176px;height:134px;background:linear-gradient(135deg,#dfe3d8,#c6cfd6)}
.social{display:flex;gap:6px}
.social i{width:16px;height:16px;border-radius:50%;background:#666}
.cards{display:flex;gap:6px;margin-top:10px}
.cards i{width:34px;height:22px;background:#555;border-radius:2px}
.nl-input{display:flex;margin-top:6px}
.nl-input span{width:150px;height:22px;background:var(--white)}
.nl-input b{background:var(--blue);color:var(--white);font-size:9px;line-height:22px;padding:0 8px}
.copy{left:0;top:2160px;width:1200px;height:32px;background:var(--navy);color:#cfd8e6;font-size:9px;text-align:center;line-height:32px}
</style>
</head>
<body>

<header class="site-header abs">
  <div class="brand abs"><span class="brand-mark"></span><span class="brand-name">Rolling<br>Nest</span></div>
  <div class="top-links abs"><span><i></i>Log In</span><span><i></i>My Account</span><span><i></i>My Wishlist</span><span><i></i>Checkout</span></div>
  <div class="search abs"><input value="Search products"><button aria-label="Search"></button></div>
  <div class="cart abs">
    <svg width="22" height="20" viewBox="0 0 22 20"><path d="M1 2h4l3 11h10l3-8H7" fill="none" stroke="#fff" stroke-width="2"/><circle cx="9" cy="17" r="2" fill="#fff"/><circle cx="17" cy="17" r="2" fill="#fff"/></svg>
    <div><b>$0.00</b><small>0 items</small></div>
  </div>
</header>

<nav class="main-nav abs"><a class="active">HOME</a><a>PRODUCTS</a><a>SALE</a><a>ABOUT US</a><a>CONTACT US</a></nav>

<section class="hero abs" role="img" aria-label="Photo of a skater's sneaker resting on a skateboard">
  <h1 class="abs">Keep Your Board<br>Where You Want It!</h1>
  <span class="btn abs">Shop The Collection</span>
  <div class="dots abs"><i></i><i></i><i></i></div>
</section>

<h2 class="sec-title welcome-title abs">Welcome to Rolling Nest Skateboard Stand</h2>
<div class="welcome-box abs">
  <h3>ONE STAND, ANY ROOM</h3>
  <p>The stand holds every board upright and keeps wheels clear of your walls. No drilling, no mounting, no tools. Set it in a hallway, garage or bedroom and move it whenever you like. Sturdy build, simple design and quick to tidy up.</p>
  <span class="more">Read more »</span>
</div>
<h2 class="sec-title video-title abs">View video</h2>
<div class="video abs" role="img" aria-label="Product video preview showing the stand holding skateboards">
  <svg width="60" height="42" viewBox="0 0 60 42"><rect width="60" height="42" rx="8" fill="#222" opacity=".8"/><path d="M24 12l14 9-14 9z" fill="#fff"/></svg>
</div>

<aside>
  <div class="promo promo-clear abs"><div class="label">CLEARANCE</div><div style="font-size:11px">Up To</div><div class="big">90%</div><div class="ph" role="img" aria-label="Skateboards on the stand"></div><span class="mini">Shop Now</span></div>
  <div class="promo promo-ship abs"><div class="big" style="font-size:22px;line-height:28px">FREE</div><div class="label">SHIPPING</div><div class="ph" role="img" aria-label="Delivery truck"></div><span class="mini">Order Over $50.00</span></div>
  <div class="promo promo-dummy abs"><div class="ph" style="height:96px" role="img" aria-label="Stand with boards in a home"></div><span class="mini">Buy Now</span><div class="label" style="margin-top:10px">NO DRILLING</div><div style="font-size:10px">Place it anywhere</div></div>
</aside>

<div class="popular-bar abs">MOST POPULAR</div>
<div class="grid abs">
  <div class="card"><div class="ph t-white" role="img" aria-label="White and blue skateboard stand"></div><span class="sale">SALE</span><h4>NEST STAND – OCEAN BLUE</h4><div class="meta"><span>Holds 1 board</span><span>♥ 24</span></div><div class="row"><span class="stars">★★★★★</span><span class="price">$ 39.00</span></div><div class="actions"><span>Add To Cart</span><i></i></div></div>
  <div class="card"><div class="ph t-green" role="img" aria-label="Lime green skateboard stand"></div><span class="sale">SALE</span><h4>NEST STAND – LIME GREEN</h4><div class="meta"><span>Holds 1 board</span><span>♥ 18</span></div><div class="row"><span class="stars">★★★★★</span><span class="price">$ 39.00</span></div><div class="actions"><span>Add To Cart</span><i></i></div></div>
  <div class="card"><div class="ph t-cream" role="img" aria-label="Cream skateboard stand"></div><h4>NEST STAND – CREAM</h4><div class="meta"><span>Holds 1 board</span><span>♥ 12</span></div><div class="row"><span class="stars">★★★★☆</span><span class="price">$ 42.00</span></div><div class="actions"><span>Add To Cart</span><i></i></div></div>
  <div class="card"><div class="ph t-grey" role="img" aria-label="Grey skateboard stand"></div><h4>NEST STAND – STONE GREY</h4><div class="meta"><span>Holds 1 board</span><span>♥ 9</span></div><div class="row"><span class="stars">★★★★☆</span><span class="price">$ 42.00</span></div><div class="actions"><span>Add To Cart</span><i></i></div></div>
  <div class="card"><div class="ph t-red" role="img" aria-label="Red skateboard stand"></div><span class="sale">SALE</span><h4>NEST STAND – CHERRY RED</h4><div class="meta"><span>Holds 1 board</span><span>♥ 21</span></div><div class="row"><span class="stars">★★★★★</span><span class="price">$ 39.00</span></div><div class="actions"><span>Add To Cart</span><i></i></div></div>
  <div class="card"><div class="ph t-wood" role="img" aria-label="Three skateboards held in a row of stands"></div><h4>FAMILY PACK – 3 STANDS</h4><div class="meta"><span>Holds 3 boards</span><span>♥ 31</span></div><div class="row"><span class="stars">★★★★★</span><span class="price">$ 99.00</span></div><div class="actions"><span>Add To Cart</span><i></i></div></div>
  <div class="card"><div class="ph t-color" role="img" aria-label="Colourful skateboards in a row of stands"></div><h4>MIXED COLOUR 4-PACK</h4><div class="meta"><span>Holds 4 boards</span><span>♥ 15</span></div><div class="row"><span class="stars">★★★★☆</span><span class="price">$ 129.00</span></div><div class="actions"><span>Add To Cart</span><i></i></div></div>
  <div class="card"><div class="ph t-deck" role="img" aria-label="Longboards displayed on stands"></div><h4>LONGBOARD STAND XL</h4><div class="meta"><span>Fits 46" decks</span><span>♥ 7</span></div><div class="row"><span class="stars">★★★★☆</span><span class="price">$ 49.00</span></div><div class="actions"><span>Add To Cart</span><i></i></div></div>
</div>

<section class="news abs">
  <h2>Keep Up To Date On The Latest From Every</h2>
  <h3>Rolling Nest Skateboard Stand</h3>
  <p>Get news on new colours, bundle deals and tips for keeping every board tidy at home. We send a short note once a month and never share your details with anyone.</p>
  <div class="signup"><span class="ico"></span><div class="field"><small>ENTER YOUR EMAIL ADDRESS</small><div class="line"><span></span><b>SUBMIT</b></div></div></div>
</section>
<div class="news-photo abs" role="img" aria-label="Kids sitting outdoors with their skateboards"></div>

<div class="features abs">
  <div class="feature"><span class="circle" style="background:var(--green)"><svg width="24" height="24" viewBox="0 0 24 24"><path d="M5 12l5 5 9-10" fill="none" stroke="#fff" stroke-width="3"/></svg></span><div><b>Returns</b><small>Easy 30 days</small></div></div>
  <div class="feature"><span class="circle" style="background:#9aa3ad"><svg width="24" height="24" viewBox="0 0 24 24"><circle cx="12" cy="12" r="9" fill="none" stroke="#fff" stroke-width="2"/><text x="12" y="17" font-size="13" text-anchor="middle" fill="#fff" font-family="Arial">?</text></svg></span><div><b>QUESTIONS?</b><small>Read FAQ's</small></div></div>
  <div class="feature"><span class="circle" style="background:var(--blue)"><svg width="26" height="20" viewBox="0 0 26 20"><rect x="1" y="3" width="15" height="11" fill="#fff"/><path d="M16 7h5l4 4v3h-9z" fill="#fff"/><circle cx="6" cy="16" r="2.5" fill="#fff"/><circle cx="20" cy="16" r="2.5" fill="#fff"/></svg></span><div><b>DELIVERY</b><small>Information</small></div></div>
  <div class="feature"><span class="circle" style="background:var(--cyan)"><svg width="22" height="22" viewBox="0 0 22 22"><path d="M5 2l4 4-2 3c1 3 3 5 6 6l3-2 4 4-3 3C9 20 2 13 2 5z" fill="#fff"/></svg></span><div><b>LET US HELP</b><small>Contact Us</small></div></div>
</div>

<footer class="site-footer abs">
  <div class="map abs" role="img" aria-label="Location map"></div>
  <div class="foot-col abs" style="left:370px"><h5>QUICK LINKS</h5>Home<br>About<br>Products<br>Specials<br>Contact</div>
  <div class="foot-col abs" style="left:520px"><h5>ADDRESS</h5>48 Ridgeview Lane,<br>Maplewood<br>Ph: +1 555 014 2290<br>E-mail: hello@rollingnest.example</div>
  <div class="foot-col abs" style="left:720px"><h5>INFORMATION</h5><div style="margin-top:40px;display:flex;align-items:center;gap:8px">FOLLOW US <span class="social"><i></i><i></i><i></i></span></div></div>
  <div class="foot-col abs" style="left:900px"><h5 style="font-size:12px">Don't Miss Out</h5>Sign up for our Weekly Email<div class="nl-input"><span></span><b>SIGN UP</b></div><div class="cards"><i></i><i></i><i></i><i></i></div></div>
</footer>
<div class="copy abs">Copyright © 2024 Rolling Nest. All rights reserved. www.rollingnest.example</div>

</body>
</html>
```